Larkspur Ridge Management - Business Cards

I need business cards. My current logo was designed by a designer at this site and I very much like and am happy with the results. I would like a business card that is trendy, unique, current yet professional. I deal with high net worth clients daily

Target Market(s)

Out of state investors looking to get into the rental market in Ohio

Industry/Entity Type

Property Management, Consulting

Contact Information for Business Card

Name, Title (Chief Financial Officer) office phone number (555) 817-3094 website address larkridgemgmt.example

Font styles to use
Sans Serif

Colors
0054AA
0677BA
7BADD7
CADEEF
E8F1F8
0094D4
00A9DD
6FCCEA
C7EBF8
E9F6FB
00AB8E
00BBA5
67D7C9
C6EFE9
E9F9F6

```html
<!DOCTYPE html>
<html lang="en">
<head>
<meta charset="UTF-8">
<title>Larkspur Ridge Management – Business Cards</title>
<link href="https://fonts.googleapis.com/css2?family=Montserrat:wght@500;600;700&display=swap" rel="stylesheet">
<style>
  :root {
    --navy: #25365e;
    --red: #d7262e;
    --card-white: #ffffff;
    --backdrop: #e7e8ea;
    --text-light: #ffffff;
  }
  * { box-sizing: border-box; margin: 0; padding: 0; }
  html, body {
    width: 874px;
    height: 1200px;
    overflow: hidden;
  }
  body {
    background: var(--backdrop);
    font-family: "Montserrat", sans-serif;
    display: flex;
    flex-direction: column;
    align-items: center;
    justify-content: center;
    gap: 80px;
  }
  .card {
    width: 560px;
    height: 320px;
    background: var(--card-white);
    box-shadow: 4px 6px 10px rgba(0, 0, 0, 0.28);
    display: flex;
    overflow: hidden;
  }
  .card-front {
    align-items: center;
    justify-content: center;
  }
  .brand-name {
    color: var(--navy);
    font-weight: 700;
    text-transform: uppercase;
    text-align: center;
    line-height: 1.1;
    display: flex;
    flex-direction: column;
    align-items: center;
    gap: 10px;
  }
  .brand-mark {
    width: 14px;
    height: 14px;
    background: var(--navy);
  }
  .card-front .brand-name { font-size: 30px; }
  .card-back .brand-name { font-size: 19px; }
  .card-back__brand {
    width: 245px;
    display: flex;
    align-items: center;
    justify-content: center;
    padding: 0 16px;
  }
  .card-back__details {
    flex: 1;
    background: var(--navy);
    padding: 0 0 0 34px;
    display: flex;
    flex-direction: column;
    justify-content: center;
  }
  .holder-name {
    color: var(--red);
    font-weight: 600;
    font-size: 32px;
    line-height: 1;
  }
  .holder-title {
    color: var(--text-light);
    font-weight: 500;
    font-size: 14px;
    letter-spacing: 0.4px;
    margin-top: 6px;
  }
  .contact-list {
    list-style: none;
    margin-top: 24px;
    display: flex;
    flex-direction: column;
    gap: 14px;
  }
  .contact-item {
    display: flex;
    align-items: center;
    gap: 12px;
    color: var(--text-light);
    font-weight: 500;
    font-size: 15px;
    letter-spacing: 0.4px;
  }
  .contact-icon {
    width: 22px;
    height: 22px;
    flex-shrink: 0;
  }
</style>
</head>
<body>

  <section class="card card-front" aria-label="Business card front">
    <div class="brand-name">
      <span class="brand-mark"></span>
      <span>Larkspur Ridge</span>
      <span>Management</span>
    </div>
  </section>

  <section class="card card-back" aria-label="Business card back">
    <div class="card-back__brand">
      <div class="brand-name">
        <span class="brand-mark"></span>
        <span>Larkspur Ridge</span>
        <span>Management</span>
      </div>
    </div>
    <div class="card-back__details">
      <p class="holder-name">Your Name</p>
      <p class="holder-title">Chief Financial Officer</p>
      <ul class="contact-list">
        <li class="contact-item">
          <svg class="contact-icon" viewBox="0 0 24 24" aria-hidden="true">
            <path fill="#d7262e" d="M3 8c0-3 4-4 9-4s9 1 9 4v1.5c0 .8-.7 1.3-1.5 1.1l-2.8-.7c-.6-.2-1-.7-1-1.3V7.5c-1.2-.4-2.4-.5-3.7-.5s-2.5.1-3.7.5v1.1c0 .6-.4 1.1-1 1.3l-2.8.7C3.7 10.8 3 10.3 3 9.5Z"/>
            <path fill="#d7262e" d="M7.5 11h9l3 7.5c.2.8-.3 1.5-1.1 1.5H5.6c-.8 0-1.3-.7-1.1-1.5Z"/>
            <circle cx="12" cy="15.5" r="2.3" fill="#25365e"/>
          </svg>
          <span>(555) 817-3094</span>
        </li>
        <li class="contact-item">
          <svg class="contact-icon" viewBox="0 0 24 24" fill="none" stroke="#d7262e" stroke-width="1.6" aria-hidden="true">
            <circle cx="12" cy="12" r="9.5"/>
            <ellipse cx="12" cy="12" rx="4.2" ry="9.5"/>
            <line x1="2.5" y1="12" x2="21.5" y2="12"/>
            <line x1="4" y1="7" x2="20" y2="7"/>
            <line x1="4" y1="17" x2="20" y2="17"/>
          </svg>
          <span>larkridgemgmt.example</span>
        </li>
      </ul>
    </div>
  </section>

</body>
</html>
```